New All Natural Skin Care company needs logo and label design for a new skin serum product

We need a name, logo, and label design for a new company that is producing an all in one all natural highly effective skin serum. The end result should include image imposed on clear 120z plastic bottle

We would like to see designs that promote an authentic, all natural, highly effective brand image. We need the product to standout amongst the crowded store shelves. The target customer includes Greenmarrow, Pell Cortway, and other upscale supermarket and drug store chains. This is an all in one skin product that aims to simplify a very crowded field and over cluttered market segment.

Reason: Need some great designs. Something very unique that stands out on the crowded store shelves.

Target Market(s)

men and woman, 25 years and older, who are healthy and care about their skin appearance

Industry/Entity Type

Plastic

Requirements
Nice to have
• I was inspired by a juice company called Fernjarpress.example Please check it out for inspiration.

I am also inspired by mistolvane.example but am looking for more modern approach

I am interested in seeing the ingredients and benefits listed somewhere on the bottle. Here are some of them:

Jojoba Oil-moisturizing and soothing
Vitamin A-Anti Aging, Reduces wrinkles
Vitamin B-Anti Inflammatory
Vitamin C-Promote Collagen
Vitamin D3-Helps skin conditions
Vitamin E-Antioxidant
Squalene-Natural Moisturizing
Calsium Gluconate-Anti-Microbial
Acai-
Aloe-
Japanese Green Tea-anti-inflammatory
Glycerin-Moisturizing

```html
<!DOCTYPE html>
<html lang="en">
<head>
<meta charset="utf-8">
<title>Verdant Pith – All-in-One Skin Treatment Label</title>
<link rel="stylesheet" href="https://fonts.googleapis.com/css2?family=Arimo:wght@400;700&family=Roboto+Condensed:wght@700&family=Crimson+Text:wght@400&family=Merriweather:wght@700&display=swap">
<style>
  :root {
    --paper: #ffffff;
    --leaf: #2aa52a;
    --forest: #1d6b12;
    --benefit: #2b7a1e;
    --citrus: #f7a21b;
    --ink: #222222;
    --brand-ink: #3a3a3a;
    --glass-edge: #e6e6e6;
    --glass-mid: #f7f7f7;
    --glass-line: #dcdcdc;
    --cap-light: #fbfbfb;
    --cap-shade: #e2e2e2;
  }
  * { margin: 0; padding: 0; box-sizing: border-box; }
  html, body {
    width: 894px;
    height: 1200px;
    overflow: hidden;
    background: var(--paper);
  }
  .label {
    position: relative;
    width: 894px;
    height: 1200px;
  }
  .bottle-cap {
    position: absolute;
    left: 432px;
    top: 198px;
    width: 114px;
    height: 84px;
    border-radius: 8px 8px 3px 3px;
    background: linear-gradient(90deg, var(--cap-shade) 0%, var(--cap-light) 30%, var(--paper) 55%, var(--cap-light) 75%, var(--cap-shade) 100%);
    border: 1px solid var(--glass-line);
  }
  .bottle-body {
    position: absolute;
    left: 378px;
    top: 284px;
    width: 220px;
    height: 638px;
    border-radius: 14px 14px 22px 22px;
    background: linear-gradient(90deg, var(--glass-edge) 0%, var(--glass-mid) 8%, var(--paper) 30%, var(--paper) 70%, var(--glass-mid) 92%, var(--glass-edge) 100%);
    border: 1px solid var(--glass-line);
  }
  .bottle-reflection {
    position: absolute;
    left: 382px;
    top: 926px;
    width: 212px;
    height: 84px;
    background: linear-gradient(180deg, var(--glass-mid) 0%, rgba(255,255,255,0) 100%);
  }
  .brand-mark {
    position: absolute;
    left: 0;
    width: 894px;
    top: 360px;
    display: flex;
    align-items: center;
    justify-content: center;
    gap: 12px;
    padding-left: 80px;
  }
  .brand-mark__dot {
    width: 30px;
    height: 30px;
    border-radius: 50%;
    background: var(--citrus);
  }
  .brand-mark__name {
    font-family: "Crimson Text", serif;
    font-size: 26px;
    color: var(--brand-ink);
  }
  .headline {
    position: absolute;
    left: 0;
    width: 894px;
    padding-left: 80px;
    text-align: center;
    top: 476px;
    font-family: "Roboto Condensed", sans-serif;
    font-weight: 700;
    font-size: 29px;
    color: var(--leaf);
    letter-spacing: 0.2px;
  }
  .subhead {
    position: absolute;
    left: 0;
    width: 894px;
    padding-left: 80px;
    text-align: center;
    top: 508px;
    font-family: "Crimson Text", serif;
    font-size: 16px;
    color: var(--ink);
  }
  .ingredients {
    position: absolute;
    left: 0;
    width: 894px;
    padding-left: 80px;
    text-align: center;
    top: 540px;
    font-family: "Arimo", sans-serif;
    font-weight: 700;
    font-size: 13px;
    line-height: 16px;
    color: var(--citrus);
  }
  .benefits {
    position: absolute;
    left: 420px;
    top: 610px;
    list-style: none;
    font-family: "Arimo", sans-serif;
    font-size: 12.5px;
    line-height: 15px;
    color: var(--benefit);
  }
  .tagline {
    position: absolute;
    left: 0;
    width: 894px;
    padding-left: 80px;
    text-align: center;
    top: 765px;
    font-family: "Arimo", sans-serif;
    font-weight: 700;
    font-size: 17px;
    color: var(--forest);
  }
  .brand-band {
    position: absolute;
    left: 396px;
    top: 790px;
    width: 186px;
    height: 31px;
    background: var(--forest);
    display: flex;
    align-items: center;
    justify-content: center;
    font-family: "Merriweather", serif;
    font-weight: 700;
    font-size: 16px;
    color: var(--paper);
  }
</style>
</head>
<body>
  <main class="label">
    <div class="bottle-cap" role="img" aria-label="White screw cap of the bottle"></div>
    <div class="bottle-body" role="img" aria-label="Clear plastic serum bottle"></div>
    <div class="bottle-reflection" aria-hidden="true"></div>

    <div class="brand-mark">
      <span class="brand-mark__dot" aria-hidden="true"></span>
      <span class="brand-mark__name">Verdant Pith</span>
    </div>
    <h1 class="headline">ALL NATURAL</h1>
    <p class="subhead">All-in-One Skin Treatment</p>
    <p class="ingredients">With Acai Berries, Aloe Vera<br>&amp; Jojoba Oil</p>
    <ul class="benefits">
      <li>Soothing</li>
      <li>Anti-Aging</li>
      <li>Antioxidant</li>
      <li>Moisturizing</li>
      <li>Anti-Microbial</li>
      <li>Anti Inflammatory</li>
      <li>Reduces Wrinkles</li>
      <li>Promote Collagen</li>
      <li>Skin Condition Therapy</li>
    </ul>
    <p class="tagline">ONLY EVER</p>
    <div class="brand-band">Verdant Pith</div>
  </main>
</body>
</html>
```